Create an awesome website for a medical clinic

This is a new website for a doctor's office. The site should be clean and modern, easy to navigate.

This is a wellness clinic, we want to help our clients have a healthy, active lifestyle. It should be friendly and inviting, and easy for them to call or schedule an appointment.

The site should be responsive and designed using the attached Bootstrap 3 PSD.

We will provide stock photos, until then please use stock photos from:

photoharvestbin.net or
lumapicturevault.net (preferred)

Some example sites of clean and modern designs that we like:

https://tarnelspine.example/
http://walkpastjoints.example/
http://feelingbrisker.example/

Also attached is a temporary logo you can use.
Updates

Reason: Thank you everyone for your great designs - we need a little more time so I'm extending the project.

Need extra days to review

Also, the colors in the new logo I just linked to are the final colors of the logo, so feel free to use any complimentary colors to it.

Hi everyone, The boss wants to change the layout of the site a little bit - here's the revised layout: https://www.filecrate.example/s/q8vn31kd2pxe74rt/memo%2011_29_2017.pdf?dl=0 And the graphic assets you can use are here: https://www.filecrate.example/s/q8vn31kd2pxe74rt/memo%2011_29_2017.pdf?dl=0 Feel free to change the background color of the "topbar", and change the icons of the "why people trust us" if you want, these are just temporary placeholders. Thanks for your patience and hard work!

Target Market(s)

People seeking medical treatment (wellness clinic)

Industry/Entity Type

Doctor

Number of Pages Required

1 page

Font styles to use
Sans Serif

Colors
0592cd
33a6d7
abd037
9bcb3c

Requirements
Must have
• The home page should have: a strong hero image/slideshow, clinic phone number should be prominent and at the top of the page (in the nav), a "what to expect" section (this is like a FAQs section - see attachment), and a strong call to action (a button to call or schedule an appointment).
• The what to expect section is useful so that prospective clients can determine if we're a good fit for them or not. It's a basic, first-step pre-qualification block of information.
• Social media icons which links to our social media profiles should be included.
Nice to have
• - Link to 3 most recent blog entries
• - Testimonials
• - How a multilevel nav menu looks.

```html
<!DOCTYPE html>
<html lang="en">
<head>
<meta charset="utf-8">
<title>Verdant Care Clinic</title>
<link href="https://fonts.googleapis.com/css2?family=Lato:wght@400;700&family=Roboto:wght@400;700&family=Poppins:wght@500;600&display=swap" rel="stylesheet">
<style>
:root{
  --green:#8dc63f;
  --green-dark:#1f9d3a;
  --lime:#c1ec52;
  --blue:#0592cd;
  --blue-mid:#0f98c8;
  --teal:#1f9a7a;
  --leaf:#8dc54a;
  --pale:#e8f5f9;
  --text-grey:#666;
  --dark:#333;
  --white:#fff;
}
*{margin:0;padding:0;box-sizing:border-box}
html,body{width:1040px;height:1200px;overflow:hidden;background:var(--white);font-family:'Lato',sans-serif}
.page{position:relative;width:1040px;height:1200px}
.brand{position:absolute;left:52px;top:20px;font-family:'Lato',sans-serif;font-weight:700;color:var(--green-dark);line-height:1}
.brand .name{font-size:31px;letter-spacing:0.5px;display:block}
.brand .sub{font-size:14px;letter-spacing:0.6px;display:block;margin-top:3px}
.contact{position:absolute;top:30px;display:flex;align-items:center;gap:6px}
.contact .ring{width:31px;height:31px;border:1.5px solid #ddd;border-radius:50%;display:flex;align-items:center;justify-content:center}
.contact .label{font-family:'Poppins',sans-serif;font-size:8px;font-weight:600;color:var(--dark);line-height:1.4}
.contact .value{font-family:'Poppins',sans-serif;font-size:8px;color:var(--dark);font-weight:500}
.call{left:528px}
.mail{left:651px}
.appointment{position:absolute;left:795px;top:26px;width:194px;height:40px;background:var(--green);border:2px solid #a8d84f;color:var(--white);font-family:'Roboto',sans-serif;font-size:16px;display:flex;align-items:center;gap:12px;padding-left:14px}
.nav{position:absolute;left:51px;top:86px;width:937px;height:59px;background:linear-gradient(90deg,var(--green),#5bb38a 40%,#2aa3b9 75%,var(--blue))}
.nav a{position:absolute;top:0;height:59px;line-height:59px;color:var(--white);font-size:15.5px;text-decoration:none;transform:translateX(-50%);white-space:nowrap}
.nav .active{background:var(--lime);color:var(--dark);width:114px;text-align:center;left:75px;transform:none}
.hero-photo{position:absolute;left:51px;top:149px;width:421px;height:402px;background:linear-gradient(160deg,#dfeef0,#c9dde0 55%,#b8d5a8)}
.hero-panel{position:absolute;left:472px;top:149px;width:516px;height:402px;background:linear-gradient(150deg,#7fc35a 0%,#3aa79c 40%,#0893cf 85%)}
.hero-panel h1{position:absolute;left:58px;top:88px;width:380px;font-family:'Poppins',sans-serif;font-weight:600;font-size:26px;line-height:33px;color:var(--white)}
.hero-panel p{position:absolute;left:58px;top:159px;width:385px;font-size:15px;line-height:19px;color:var(--white)}
.hero-panel .rule{position:absolute;left:57px;top:228px;width:393px;height:1px;background:rgba(255,255,255,.8)}
.hero-panel .cta{position:absolute;left:58px;top:244px;width:170px;height:43px;border:2px solid var(--white);color:var(--white);font-family:'Poppins',sans-serif;font-weight:600;font-size:16px;display:flex;align-items:center;justify-content:center}
.feature{position:absolute;top:551px;height:217px;color:var(--white);padding:28px 31px}
.feature h2{font-family:'Roboto',sans-serif;font-weight:400;font-size:21px;margin-bottom:17px}
.feature p{font-size:13.5px;line-height:17.5px;width:250px}
.feature .more{position:absolute;left:31px;top:149px;width:97px;height:31px;border:1px solid var(--white);font-size:13px;display:flex;align-items:center;justify-content:center}
.f1{left:51px;width:313px;background:var(--blue-mid)}
.f2{left:364px;width:312px;background:var(--teal)}
.f3{left:676px;width:312px;background:var(--leaf);padding-left:34px}
.hours{list-style:none;width:222px;margin-top:-4px}
.hours li{display:flex;justify-content:space-between;font-size:13.5px;border-bottom:1px solid rgba(255,255,255,.85);padding:7px 2px 8px;margin-bottom:11px}
.about{position:absolute;left:0;top:768px;width:1040px;height:432px;background:var(--pale);text-align:center}
.about h2{margin-top:56px;font-family:'Roboto',sans-serif;font-weight:400;font-size:40px;color:#7bb91f}
.about h2 b{font-weight:700}
.about p{margin:12px auto 0;width:680px;font-size:20px;line-height:28px;color:var(--text-grey)}
.about .rule{width:155px;height:1px;background:linear-gradient(90deg,#2aa3b9,#4fb56f);margin:16px auto 0}
.services{position:absolute;left:0;top:246px;width:1040px;height:150px}
.services svg{position:absolute;left:0;top:0;display:block}
</style>
</head>
<body>
<div class="page">
  <div class="brand"><span class="name">VERDANT</span><span class="sub">CARE CLINIC</span></div>

  <div class="contact call">
    <span class="ring"><svg width="12" height="12" viewBox="0 0 24 24"><path d="M6.6 10.8a15 15 0 0 0 6.6 6.6l2.2-2.2c.3-.3.7-.4 1-.2 1.1.4 2.3.6 3.6.6.6 0 1 .4 1 1V20c0 .6-.4 1-1 1A17 17 0 0 1 3 4c0-.6.4-1 1-1h3.5c.6 0 1 .4 1 1 0 1.3.2 2.5.6 3.6.1.3 0 .7-.2 1z" fill="#333"/></svg></span>
    <div><div class="label">Call Us</div><div class="value">(555) 014 2273</div></div>
  </div>
  <div class="contact mail">
    <span class="ring"><svg width="12" height="10" viewBox="0 0 24 18"><path d="M0 0h24v2L12 10 0 2z M0 5l12 8 12-8v13H0z" fill="#333"/></svg></span>
    <div><div class="label">Email Us</div><div class="value" style="font-size:7px">info@verdantcare.example</div></div>
  </div>
  <div class="appointment">
    <svg width="26" height="26" viewBox="0 0 26 26"><circle cx="11" cy="8" r="6" fill="#fff"/><path d="M1 24c0-6 4-9 10-9s10 3 10 9z" fill="#fff"/><circle cx="21" cy="21" r="4" fill="#8dc63f" stroke="#fff" stroke-width="1.5"/><path d="M21 19v4M19 21h4" stroke="#fff" stroke-width="1.3"/></svg>
    Get Appointment
  </div>

  <nav class="nav">
    <a class="active">Home</a>
    <a style="left:278px">About Us</a>
    <a style="left:411px">Our Patients</a>
    <a style="left:578px">Our Treatments</a>
    <a style="left:727px">Galliers</a>
    <a style="left:854px">Contact Us</a>
  </nav>

  <div class="hero-photo" role="img" aria-label="Smiling dentist in a white coat beside a patient seated in a green dental chair"></div>
  <section class="hero-panel">
    <h1>It is a long established fact by readable content</h1>
    <p>There are many variations of passages of Lorem Ipsum available, but the majority have suffered alteration in some form, by injected humour,</p>
    <div class="rule"></div>
    <div class="cta">ALTERATION</div>
  </section>

  <section class="feature f1">
    <h2>Aublishing software</h2>
    <p>The generated Lorem Ipsum is therefore always free from repetition, injected humour, or non-characteristic.</p>
    <div class="more">Read more</div>
  </section>
  <section class="feature f2">
    <h2>Publishing software</h2>
    <p>The generated Lorem Ipsum is therefore always free from repetition, injected humour, or non-characteristic.</p>
    <div class="more">Read more</div>
  </section>
  <section class="feature f3">
    <h2>Publishing software</h2>
    <ul class="hours">
      <li><span>Cariopng - Criond</span><span>09.00 - 16.00</span></li>
      <li><span>Cariopngy</span><span>09.30 - 16.00</span></li>
      <li><span>Cariopngy</span><span>09.30 - 15.00</span></li>
    </ul>
  </section>

  <section class="about">
    <h2>We are in <b>Lorem Ipsum...</b></h2>
    <p>Randomised words which don't look even slightly believable. If you are going to use a passage of Lorem Ipsum, you need to be sure there</p>
    <div class="rule"></div>
    <div class="services">
      <svg width="1040" height="150" viewBox="0 0 1040 150">
        <defs>
          <linearGradient id="ringGrad" x1="0" y1="0" x2="0" y2="1"><stop offset="0" stop-color="#7dc14a"/><stop offset="1" stop-color="#1a96c8"/></linearGradient>
        </defs>
        <g fill="none" stroke="url(#ringGrad)" stroke-width="2.5">
          <circle cx="164" cy="73" r="72"/>
          <circle cx="403" cy="73" r="72"/>
          <circle cx="640" cy="73" r="72"/>
          <circle cx="876" cy="73" r="72"/>
        </g>
        <g fill="none" stroke="url(#ringGrad)" stroke-width="2.5" stroke-linejoin="round">
          <rect x="157" y="37" width="14" height="10"/>
          <path d="M150 47h28a4 4 0 0 1 4 4v60h-36V51a4 4 0 0 1 4-4z"/>
          <path d="M146 66h36M146 100h36"/>
          <path d="M160 75h8v6h6v8h-6v6h-8v-6h-6v-8h6z"/>
          <path d="M385 40c0 30 36 40 36 70M421 40c0 30-36 40-36 70"/>
          <path d="M389 50h28M395 62h16M395 88h16M389 100h28"/>
          <path d="M604 106h72v-12h-72z M620 94v-5h14v5"/>
          <path d="M608 84h24"/>
          <path d="M656 94V72l-12-14"/>
          <path d="M644 46l10-10 8 8-10 10z M636 54l8-8 8 8-8 8z"/>
          <path d="M840 106h72v-12h-72z M856 94v-5h14v5"/>
          <path d="M844 84h24"/>
          <path d="M892 94V72l-12-14"/>
          <path d="M880 46l10-10 8 8-10 10z M872 54l8-8 8 8-8 8z"/>
        </g>
      </svg>
    </div>
  </section>
</div>
</body>
</html>
```